Employees at T&M Gale Power Solutions need new modern business cards

We need new business cards that showcase our new rebranded logo. We are seeking modern, clean, fresh, attractive cards while still being professional. We want to stand out. A little bit about us: we work in Canada and the USA. We offer Technical Field Advisors to support wind turbine manufacturers through the construction phase of wind farms. I am attaching a mock inspiration picture to lead you in the direction we want to see this go. Also, FYI We have approx. 10/11 different employees that would need their own card. Let me know when you would need everyone's name. We would love to see some black and white options as well as color copies- when using colors we want green to be the dominant color with accents for blue and orange (colors should match our logo). I have also attached copies of our old business card for reference.

Contact Information for Business Card

Name, Telephone, Email, address, company name, website. EXAMPLE: Hugh Marlow, HughMarlow@tandmgale.example, 555-381-4926, 217763 Birch Line #9, Elmhurst, ON X1Y 2Z3, www.tandmgale.example

Colors
0054AA
0677BA
7BADD7
CADEEF
E8F1F8
00AB8E
00BBA5
67D7C9
C6EFE9
E9F9F6
F0912C
F2A743
F7CA91
FBE8D2
FDF5EE

Requirements
Must have
• 2 sided business card

```html
<!DOCTYPE html>
<html lang="en">
<head>
<meta charset="utf-8">
<title>T&amp;M Gale Power Solutions – Business Card</title>
<link href="https://fonts.googleapis.com/css2?family=Roboto:wght@400;700&display=swap" rel="stylesheet">
<style>
  :root {
    --page-bg: #d9d9d9;
    --card-white: #f7f7f7;
    --card-dark: #333333;
    --brand-green: #3dae49;
    --brand-orange: #f0912c;
    --text-light: #ffffff;
  }
  * { margin: 0; padding: 0; box-sizing: border-box; }
  html, body { width: 1200px; height: 1200px; overflow: hidden; }
  body {
    background: var(--page-bg);
    font-family: "Roboto", Arial, sans-serif;
    position: relative;
  }
  .card {
    position: absolute;
    left: 240px;
    width: 720px;
    height: 411px;
    border-radius: 26px;
    overflow: hidden;
  }
  .card--front { top: 150px; background: var(--card-white); }
  .card--back { top: 640px; background: var(--card-dark); }
  .card__split { position: absolute; inset: 0; width: 100%; height: 100%; }

  .brand { position: absolute; }
  .brand__dot {
    display: block;
    border-radius: 50%;
    background: var(--brand-green);
  }
  .brand__name {
    display: block;
    color: var(--brand-green);
    font-weight: 700;
    text-transform: uppercase;
    letter-spacing: 0.06em;
    line-height: 1.1;
  }
  .card--front .brand { left: 50px; top: 48px; width: 230px; }
  .card--front .brand__dot { width: 92px; height: 92px; margin: 0 0 14px 64px; }
  .card--front .brand__name { font-size: 21px; }

  .card--back .brand { left: 0; right: 0; top: 106px; text-align: center; }
  .card--back .brand__dot { width: 130px; height: 130px; margin: 0 auto 24px; }
  .card--back .brand__name { font-size: 30px; }

  .contact {
    position: absolute;
    right: 54px;
    top: 200px;
    text-align: right;
    color: var(--text-light);
    font-size: 15.5px;
    line-height: 20px;
  }
  .contact__name {
    color: var(--brand-green);
    font-size: 25px;
    font-weight: 700;
    line-height: 30px;
    margin-bottom: 12px;
  }
  .contact__address { margin-bottom: 14px; }
  .contact__list { list-style: none; margin-right: -27px; }
  .contact__item { display: flex; justify-content: flex-end; align-items: center; gap: 13px; height: 21px; }
  .contact__icon { width: 14px; height: 14px; flex: none; }
</style>
</head>
<body>
  <section class="card card--front">
    <svg class="card__split" viewBox="0 0 720 411" preserveAspectRatio="none" aria-hidden="true">
      <polygon points="0,290 720,110 720,124 0,304" fill="var(--brand-green)"/>
      <polygon points="0,304 720,124 720,411 0,411" fill="var(--card-dark)"/>
    </svg>

    <div class="brand">
      <span class="brand__dot"></span>
      <span class="brand__name">T&amp;M Gale Power Solutions</span>
    </div>

    <div class="contact">
      <p class="contact__name">Hugh Marlow</p>
      <p class="contact__address">217763 Birch Line #9<br>Elmhurst, ON X1Y 2Z3</p>
      <ul class="contact__list">
        <li class="contact__item">555-381-4926
          <svg class="contact__icon" viewBox="0 0 16 16" aria-hidden="true"><path d="M3 1 L6 1 L7 5 L5 6.5 C6 9 7.5 10.5 9.5 11 L11 9 L15 10 L15 13 C15 14 14 15 13 15 C6.5 14.5 1.5 9.5 1 3 C1 2 2 1 3 1 Z" fill="var(--brand-orange)"/></svg>
        </li>
        <li class="contact__item">HughMarlow@tandmgale.example
          <svg class="contact__icon" viewBox="0 0 16 16" aria-hidden="true"><rect x="1" y="3" width="14" height="10" fill="var(--brand-orange)"/><path d="M1 3 L8 9 L15 3" fill="none" stroke="var(--card-dark)" stroke-width="1.4"/></svg>
        </li>
        <li class="contact__item">www.tandmgale.example
          <svg class="contact__icon" viewBox="0 0 16 16" aria-hidden="true"><circle cx="8" cy="8" r="7" fill="var(--brand-orange)"/><path d="M8 1 C5 4 5 12 8 15 M8 1 C11 4 11 12 8 15 M1 8 H15" fill="none" stroke="var(--card-dark)" stroke-width="1.1"/></svg>
        </li>
      </ul>
    </div>
  </section>

  <section class="card card--back">
    <div class="brand">
      <span class="brand__dot"></span>
      <span class="brand__name">T&amp;M Gale Power Solutions</span>
    </div>
  </section>
</body>
</html>
```